Simple and clean poster/flyer design needed for public speaker!

SIMPLE AND CLEAN DESIGN NEEDED FOR POSTER/FLYER

I AM a public speaker based in London (www.tobiaskernwald.com)
and I would like to have a custom-made flyer/poster
(preferably in adobe CS4 template format) that I con customize (just changing the text) for my various speeches, topics and locations

I am looking for something very simple and clean.
NO extravagance or crowded poster, but a rather beautiful clean and eye-catching design that clearly informs people what i am talking about, where and when.

Go to my website www.tobiaskernwald.com
to see the colour scheme and style that I like
my poster should be like the website, similar colours, logo, clean, simple and clear.

Summary

(1) simple and clean design
(2) design that fits my brand (see website)
(3) clear and eye-catching to promote my speeches
(4) customizable for my various talks, by simply chancing the text (Please Adobe Photoshop CS4 template format)
(5)in A3, A4, A5, A6 sizes, so i can use it for both flyers and small posters

ADDITIONS

BIG BOLD HEADLINE TO GRAP ATTENTION, greatest prominence

sub headline to explain, smaller than the headline, but still prominent on the poster

just a few bullet points to list the benefits and answer the “whats in for me”-question
this is for people who are already interested and continue reading, medium prominence.

WHERE, WHEN, HOW MUCH-information, in the lower section of the poster, little text, but clearly visible

only one point of CONTACT on my poster “www.tobiaskernwald.com”, bit big and clear so that it is very prominent

little text, effectively used
LESS IS MORE
Updates

contact me regarding logo files and any questions you may have!

for the logo files go to

https://secure.dropvaultly.com/fs/v.aspx?v=41958b2d703c9ea1f6d2

click on the folder "logo pack" to see the files

eps
jpg
png
photoshop
TIF

thanks for your interest. hope to see great designs!
I am really looking forward to it
if you have any questions, please do not hesitate to ask

Kind Regards
Tobias
 

• Simple, clean design, text sparingly used.

• The mood should be light-hearted, calm, bright, simple and friendly, comic like

• a lot of white space, calling more attention to the content

• a light blue, dark blue, white and black colour scheme as seen on the homepage (www.tobiaskernwald.com) please use the exact same colours as seen on the homepage.

White being most predominant, 2 different blue used to highlight something, black for text on white background.

• One graphic would be cool, as long as it is blue. It could be waves-like graphic, or something like the white pattern in the background, in my case just in blue on white background > http://www.lumenquietharbor.org/., I do not mean exactly this graphic and not that crowded but a simple single graphic in blue as long as it fits the theme and feel of my poster

Top o f the poster

• (a )One short bold headline (TALK TITLE) with a sub-headline below it (hook)

• or (b) headline as question (…....?) and below sub-headline offering the solution (my talk ;-) of course)

• 3 benefits as on homepage, that I can adapt for each talk (bottom right of my start site “what are you looking for?” either blue on white, or as in the page white on blue...whatever looks better and fits the design). Not sure how that looks, and if to include it!

• the bottom of the poster will have “Where”-information “when”-information “ticket price” info

• contact at the very bottom...for more into or to purchase tickets (my website and email)

If you have any questions or need clarification please write me!

Requirements
Must have
• lot of white space
• less is more - simple design
• little text, little graphics- only used when necessary to greatest effect.
• light, friendly, modern feel
• blue-color scheme

```html
<!DOCTYPE html>
<html lang="en">
<head>
<meta charset="utf-8">
<title>Tobias Kernwald – Be The Change of Life</title>
<link href="https://fonts.googleapis.com/css2?family=Questrial&family=Open+Sans:ital,wght@0,400;0,600;1,400&display=swap" rel="stylesheet">
<style>
  :root {
    --sky: #2fc4ea;
    --sky-pale: #dff4fb;
    --ink: #222629;
    --paper: #ffffff;
  }
  html, body { margin: 0; padding: 0; overflow: hidden; background: var(--paper); }
  .poster {
    position: relative;
    width: 849px;
    height: 1200px;
    overflow: hidden;
    background: var(--paper);
    font-family: "Open Sans", Arial, sans-serif;
    color: var(--ink);
  }
  .foliage {
    position: absolute;
    border-radius: 50%;
    background: radial-gradient(ellipse at center, var(--sky-pale) 0%, rgba(223,244,251,0.6) 55%, rgba(255,255,255,0) 75%);
  }
  .foliage--top { left: 300px; top: -60px; width: 600px; height: 300px; }
  .foliage--right { left: 700px; top: 330px; width: 220px; height: 420px; }
  .foliage--left { left: -80px; top: 620px; width: 420px; height: 480px; }
  .foliage--bottom { left: 560px; top: 940px; width: 320px; height: 200px; }

  .brand { position: absolute; left: 78px; top: 0; width: 130px; height: 220px; }
  .brand__mark { position: absolute; left: 38px; top: 100px; width: 54px; height: 54px; border-radius: 50%; background: var(--sky); opacity: .85; }
  .brand__name { position: absolute; left: -4px; top: 184px; white-space: nowrap; font-family: "Questrial", sans-serif; font-size: 17px; color: var(--sky); letter-spacing: .5px; }
  .brand__role { position: absolute; left: 4px; top: 206px; white-space: nowrap; font-family: "Questrial", sans-serif; font-size: 9px; color: var(--ink); letter-spacing: .6px; }

  .title-band { position: absolute; left: 0; top: 238px; width: 849px; height: 42px; background: var(--sky); }
  .title-band__text { position: absolute; right: 52px; top: 2px; margin: 0; font-family: "Questrial", sans-serif; font-weight: 400; font-size: 33px; line-height: 38px; color: var(--paper); }

  .affirmation { position: absolute; left: 54px; top: 370px; margin: 0; font-family: "Questrial", sans-serif; font-size: 30px; line-height: 36.8px; color: var(--sky); }

  .benefits { position: absolute; left: 247px; top: 370px; width: 320px; font-size: 11.8px; line-height: 16px; }
  .benefits p { margin: 0 0 16px; }
  .benefit__title { font-family: "Questrial", sans-serif; font-size: 17.5px; color: var(--sky); }

  .event { margin: 0; padding: 0; list-style: none; }
  .event li { display: flex; margin-bottom: 3px; }
  .event__label { width: 64px; flex: none; font-family: "Questrial", sans-serif; font-size: 14px; color: var(--sky); }

  .testimonials { position: absolute; left: 646px; top: 855px; width: 152px; font-size: 8.6px; line-height: 11.5px; }
  .testimonial { margin: 0 0 32px; }
  .testimonial__source { display: block; padding-left: 26px; color: var(--sky); }

  .contact-band { position: absolute; left: 0; top: 1100px; width: 849px; height: 100px; background: var(--sky); }
  .contact-band__text { position: absolute; left: 78px; top: 34px; margin: 0; font-style: italic; font-size: 17.5px; line-height: 22px; color: var(--paper); }
</style>
</head>
<body>
<div class="poster">
  <div class="foliage foliage--top" role="img" aria-label="Pale blue leaf silhouettes"></div>
  <div class="foliage foliage--right" role="img" aria-label="Pale blue leaf silhouettes"></div>
  <div class="foliage foliage--left" role="img" aria-label="Pale blue leaf silhouettes"></div>
  <div class="foliage foliage--bottom" role="img" aria-label="Pale blue leaf silhouettes"></div>

  <div class="brand">
    <div class="brand__mark"></div>
    <div class="brand__name">TOBIAS KERNWALD</div>
    <div class="brand__role">SPIRITUAL SPEAKER</div>
  </div>

  <div class="title-band"><h1 class="title-band__text">Be The Change of Life</h1></div>

  <p class="affirmation">You are a<br>beautiful<br>expression<br>of Life.<br>You are<br>worthwhile<br>because<br>you exist.<br>Life created<br>you with<br>sacred<br>worth.</p>

  <div class="benefits">
    <p><span class="benefit__title">Improve Self-Esteem</span> Aliquam et dsanisl vel ligula consectetuer suscipit. Morbi euismod enim eget neque. Donec sagittis massa. Veste dew bulum quis augue sit amet ipsum laoreet pretium. Nulla facilisi. Duis tincidunt, felis et luctus placerat, ipsum libero vestibulum sem, vitae eleum wisi ipsum a metus. Nulla a enim sed dui hendrerit lobortis. Donec lacinia vulputate magna.</p>
    <p><span class="benefit__title">Inner Peace and Calm</span> Aliquam et nisl vel ligula consectetuer suscipit. Morbi euism enim eget neque. Donec sagittis massa. DeVei tibulum quis augue sit amet ipsum laoreet pretium. Nulla facilisi. Duis tincidunt, felis et luctus placerat, ipsum libero vestibulum sem.</p>
    <p><span class="benefit__title">Greater Purpose and Meaning of Life</span><br>Duis tincidunt, felis et luctus placerat, ipsum libero vestibulum sem, vitae eleum wisi ipsum a metus. Nulla a enim sed dui hendrerit lobortis. Donec lacinia vulputate magna.</p>
    <ul class="event">
      <li><span class="event__label">Where</span><span>Riverside Hall, 12 Elm Street, London</span></li>
      <li><span class="event__label">When</span><span>Saturday 14 June, 7.00 pm – 9.00 pm</span></li>
      <li><span class="event__label">Tickets</span><span>£15 in advance, £18 on the door</span></li>
    </ul>
  </div>

  <div class="testimonials">
    <p class="testimonial">“Sagittis massa. Veste dew bulum quis augue sit amet ipsum laoreet pretium. Nulla facilisi. Duis tincidunt, felis et luctus placerat, ipsum libero vestibulum sem, vitae eleum wisi ipsum a metus. Nulla a enim sed dui hend.”<span class="testimonial__source">~customer experience</span></p>
    <p class="testimonial">“Este dewbulum quis augue sit amet ipsum laoreet pretium. Nulla facilisi. Duis tincidunt, felis et luctus placerat, ipsum libero.”<span class="testimonial__source">~customer experience</span></p>
  </div>

  <div class="contact-band">
    <p class="contact-band__text">To learn more go to www.tobiaskernwald.com<br>Contact 0700 555 0183 or email contact@tobiaskernwald.com.</p>
  </div>
</div>
</body>
</html>
```